Business Card

I need a professional business card. I would like the front to read:
Morgan Tull
Designated Pilot Examiner
407-552-3908
info@flyexamtull.net
www.flyexamtull.net

I would like the back to be matte black with a glossy black raised image of the lines from a VFR sectional chart of the local airspace in west palm. can be found at www.aeromaplane.net

Attached picture is my previous card and sectional chart I would like into lines for the back.

```html
<!DOCTYPE html>
<html lang="en">
<head>
<meta charset="utf-8">
<title>Morgan Tull — Business Card</title>
<link rel="stylesheet" href="https://fonts.googleapis.com/css2?family=Barlow:wght@400;500&family=Barlow+Semi+Condensed:wght@700;800&display=swap">
<style>
  :root {
    --stage: #e9e6e1;
    --card-black: #0b0b0b;
    --card-black-glow: #2a2a2a;
    --accent-red: #e23b3b;
    --ink-white: #ffffff;
    --ink-grey: #3a3a3a;
    --band-black: #111111;
    --band-white: #f4f4f4;
    --map-yellow: #efe79a;
    --map-blue: #bfe1ea;
    --map-violet: #c9a9d6;
  }
  * { box-sizing: border-box; margin: 0; padding: 0; }
  html, body { width: 1200px; height: 864px; overflow: hidden; }
  body {
    background: var(--stage);
    display: flex;
    align-items: center;
    justify-content: center;
    gap: 100px;
    font-family: "Barlow", sans-serif;
  }
  .card {
    position: relative;
    width: 400px;
    height: 700px;
    border-radius: 6px;
    overflow: hidden;
    box-shadow: 0 10px 30px rgba(0,0,0,.18);
  }

  /* Front */
  .card-front {
    background: radial-gradient(ellipse at 50% 45%, var(--card-black-glow) 0%, var(--card-black) 70%);
    color: var(--ink-white);
  }
  .plane-art {
    position: absolute;
    left: 60px; top: 70px;
    width: 280px; height: 150px;
    background: linear-gradient(160deg, rgba(255,255,255,.92), rgba(255,255,255,.75));
    border-radius: 4px;
  }
  .identity {
    position: absolute;
    top: 250px; left: 0; right: 0;
    text-align: center;
  }
  .name {
    font-family: "Barlow Semi Condensed", sans-serif;
    font-weight: 800;
    font-size: 50px;
    letter-spacing: 1px;
    line-height: 1;
    text-transform: uppercase;
  }
  .name-first { color: var(--accent-red); }
  .name-last { color: var(--ink-white); }
  .title {
    margin-top: 8px;
    font-size: 24px;
    letter-spacing: 1.5px;
  }
  .divider {
    width: 2px; height: 40px;
    background: var(--ink-white);
    margin: 22px auto 18px;
  }
  .contact {
    list-style: none;
    font-size: 23px;
    letter-spacing: 2px;
    line-height: 1.45;
  }
  .palm-art {
    position: absolute;
    left: 0; right: 0; bottom: 0;
    height: 170px;
    background: linear-gradient(180deg, rgba(255,255,255,0) 0%, rgba(255,255,255,.35) 45%, var(--ink-white) 88%);
  }

  /* Back */
  .card-back { background: var(--band-white); }
  .chart-art {
    position: absolute;
    inset: 0 0 180px 0;
    background: linear-gradient(135deg, var(--map-violet) 0%, var(--map-yellow) 35%, var(--map-yellow) 60%, var(--map-blue) 100%);
  }
  .back-band {
    position: absolute;
    left: 0; bottom: 0;
    width: 400px; height: 330px;
  }
  .back-plane-art {
    position: absolute;
    left: 150px; top: 430px;
    width: 170px; height: 80px;
    background: rgba(255,255,255,.9);
    border-radius: 4px;
  }
  .back-name {
    position: absolute;
    left: 0; right: 0; bottom: 44px;
    text-align: center;
    font-family: "Barlow Semi Condensed", sans-serif;
    font-weight: 800;
    font-size: 40px;
    line-height: 1;
    letter-spacing: 3px;
    color: var(--ink-grey);
    text-transform: uppercase;
  }
</style>
</head>
<body>

  <section class="card card-front" aria-label="Card front">
    <div class="plane-art" role="img" aria-label="White silhouette of a jet airliner in flight"></div>
    <div class="identity">
      <h1 class="name"><span class="name-first">Morgan</span> <span class="name-last">Tull</span></h1>
      <p class="title">Designated Pilot Examiner</p>
      <div class="divider"></div>
      <ul class="contact">
        <li>407-552-3908</li>
        <li>info@flyexamtull.net</li>
        <li>www.flyexamtull.net</li>
      </ul>
    </div>
    <div class="palm-art" role="img" aria-label="White silhouettes of palm trees along a shoreline"></div>
  </section>

  <section class="card card-back" aria-label="Card back">
    <div class="chart-art" role="img" aria-label="VFR sectional chart of the West Palm Beach airspace"></div>
    <svg class="back-band" viewBox="0 0 400 330" aria-hidden="true">
      <path d="M0 60 C120 10 280 30 400 120 L400 330 L0 330 Z" fill="var(--band-black)"/>
      <path d="M0 170 C140 150 290 165 400 210 L400 330 L0 330 Z" fill="var(--band-white)"/>
      <path d="M0 157 C140 137 290 152 400 197" fill="none" stroke="#fff" stroke-width="4"/>
      <path d="M0 147 C140 127 290 142 400 187" fill="none" stroke="var(--band-black)" stroke-width="3"/>
      <path d="M0 72 C110 30 260 45 400 130" fill="none" stroke="var(--accent-red)" stroke-width="2"/>
    </svg>
    <div class="back-plane-art" role="img" aria-label="White silhouette of a jet climbing out"></div>
    <p class="back-name">Morgan Tull</p>
  </section>

</body>
</html>
```